Flyer to University MBA Directors about my new online course

I have a new online course call Advisory Summit which helps graduates land jobs in top consultancies. I will be selling it to MBA Directors and Employability Managers in Universities. I would like a flyer that (a) sells my online course (b) introduces me (c) sells my workshops.
Updates

I don't mind if this is A4 or A5, or one or two sided, landscape or portrait. Could you please add my email to the flyer (max@advisorysummit.example)? Feel free to edit the text if it doesn't fit (e.g. replacing 'and' with &) etc.

Target Market(s)

MBA Directors & Employability Managers at Universities

Industry/Entity Type

Education

Font styles to use
Serif

Colors

Designer to choose colors to be used in the design.

Requirements
Must have
• Please add my email (max@advisorysummit.example).
• Please have one of the logos attached.
• Please add the text (or similar) in the attached.
• Please see my website (www.advisorysummit.example) for an idea of look & feel
Nice to have
• Please use a cityscape skyline as a background to one of my photos
• Please use a 2x2 matrix with icons for the 'what you get' section
• Please put the section about workshops & testimonials on the reverse
• Please use dark colours (see my website www.advisorysummit.example)

```html
<!DOCTYPE html>
<html lang="en">
<head>
<meta charset="utf-8">
<title>Advisory Summit – Flyer</title>
<link href="https://fonts.googleapis.com/css2?family=Cinzel:wght@400;600&family=Open+Sans:ital,wght@0,400;0,600;0,700;1,400&family=Oswald:wght@600;700&display=swap" rel="stylesheet">
<style>
  :root{
    --blue:#1a73c4;
    --blue-dark:#155fa3;
    --ink:#222;
    --dark:#2a2b2e;
    --hero:#2f3136;
    --grey:#8e9297;
    --grey-band:#9a9ea3;
    --panel-grey:#ececec;
    --bg:#7d7d7d;
    --white:#fff;
  }
  *{box-sizing:border-box;margin:0;padding:0}
  html,body{width:1200px;height:1200px;overflow:hidden}
  body{background:var(--bg);font-family:"Open Sans",Arial,sans-serif;color:var(--ink);position:relative}

  .page{position:absolute;width:482px;height:677px;background:var(--white);overflow:hidden}
  .page--front{left:88px;top:261px}
  .page--back{left:630px;top:262px}
  .page-bg{position:absolute;left:0;top:0;width:482px;height:677px}
  .abs{position:absolute}

  /* brand */
  .brand-mark{position:absolute;border-radius:50%}
  .brand-name{position:absolute;font-family:"Cinzel",Georgia,serif;font-weight:400;text-align:center;letter-spacing:.5px;white-space:nowrap}

  /* front headline */
  .headline{left:17px;top:118px;color:var(--white)}
  .headline__bold{font-family:"Oswald",Impact,sans-serif;font-weight:700;font-size:25px;line-height:1.05;letter-spacing:-.2px;text-transform:uppercase}
  .headline__serif{font-family:"Cinzel",Georgia,serif;font-size:19px;line-height:1.18;letter-spacing:.6px;margin-top:3px}
  .headline__with{font-size:12px;margin-top:6px}
  .headline__with b{font-weight:700}

  .section-title{font-weight:700;color:var(--blue);font-size:15.5px;line-height:1.2;text-transform:uppercase;letter-spacing:.2px}

  .ticks{list-style:none}
  .ticks li{position:relative;padding-left:13px;font-size:9.4px;line-height:1.3}
  .ticks li::before{content:"";position:absolute;left:0;top:2.5px;width:8px;height:8px;border-radius:50%;background:var(--blue)}
  .ticks li::after{content:"";position:absolute;left:2.6px;top:4.1px;width:2.2px;height:3.6px;border:solid var(--white);border-width:0 1.2px 1.2px 0;transform:rotate(40deg)}

  .career{left:16px;top:329px;width:225px}
  .career .ticks{margin-top:7px}
  .career .ticks li{margin-bottom:5.5px;color:#333}
  .career__note{font-size:9.4px;line-height:1.25;font-weight:600;color:#222;margin-top:1px}

  .get{left:267px;top:313px;width:210px;color:var(--white)}
  .get .section-title{color:var(--white)}
  .get__list{list-style:none;margin-top:9px}
  .get__item{position:relative;padding-left:27px;font-size:9.4px;line-height:1.25;font-weight:600;min-height:22px;display:flex;align-items:center}
  .get__item+.get__item{margin-top:11px}
  .get__icon{position:absolute;left:-2px;top:50%;transform:translateY(-50%);width:22px;height:22px}

  .advice{left:16px;top:473px;width:460px}
  .advice__cols{display:flex;margin-top:7px}
  .advice__col{width:236px}
  .advice__col+.advice__col{border-left:1px solid #cfd2d6;padding-left:12px;width:224px}
  .advice__col .ticks li{margin-bottom:5.2px;font-size:9.4px}

  .footer{position:absolute;left:0;bottom:0;width:482px;height:37px;background:var(--dark);display:flex;align-items:center;color:var(--white);font-size:10px}
  .footer__item{flex:1;text-align:center;display:flex;align-items:center;justify-content:center;gap:5px}
  .footer__divider{width:1.5px;height:17px;background:var(--blue)}

  /* back */
  .bio{left:16px;top:244px;width:452px}
  .bio__name{font-weight:700;color:var(--blue);font-size:20px;line-height:1.2;letter-spacing:.2px}
  .bio__text{font-size:9px;line-height:1.27;color:#111;font-weight:600;margin-top:6px}

  .pricing{left:16px;top:328px;width:452px}
  .pricing__grid{display:grid;grid-template-columns:224px 224px;row-gap:6px;margin-top:8px}
  .pricing__grid li{font-weight:600;color:#111}

  .workshops-band{position:absolute;left:0;top:395px;width:482px;height:247px;background:var(--panel-grey)}
  .workshops{left:16px;top:401px;width:454px}
  .workshops__text{font-size:9.2px;line-height:1.25;color:#222;margin-top:4px}
  .workshops__cols{display:flex;margin-top:6px}
  .workshops__cols .ticks{width:234px}
  .workshops__cols .ticks+.ticks{width:220px}
  .workshops__cols li{margin-bottom:5px;font-size:9.4px}

  .feedback{left:16px;top:552px;width:452px;height:84px;border:2px solid var(--blue);border-radius:7px}
  .feedback__title{position:absolute;left:50%;top:-11px;transform:translateX(-50%);background:var(--panel-grey);padding:0 10px;font-weight:700;color:var(--blue);font-size:15.5px;line-height:1.2;white-space:nowrap}
  .feedback__cols{display:flex;padding:12px 6px 0 6px}
  .feedback__col{width:50%;padding:0 4px}
  .feedback__col+.feedback__col{border-left:1px solid #b9bcc0}
  .quote{font-style:italic;font-size:5px;line-height:1.28;color:#222;margin-bottom:4px}
  .quote cite{color:var(--blue);font-style:italic}
</style>
</head>
<body>

<!-- FRONT -->
<section class="page page--front">
  <svg class="page-bg" viewBox="0 0 482 677" aria-hidden="false">
    <defs>
      <linearGradient id="skyline" x1="0" y1="0" x2="0" y2="1">
        <stop offset="0" stop-color="#3b3d43"/>
        <stop offset="1" stop-color="#26282c"/>
      </linearGradient>
      <linearGradient id="portrait" x1="0" y1="0" x2="0" y2="1">
        <stop offset="0" stop-color="#5a544f"/>
        <stop offset="1" stop-color="#7f7a73"/>
      </linearGradient>
    </defs>
    <g role="img" aria-label="Photo of the course author in a tweed jacket, arms crossed, in front of a city skyline">
      <rect x="0" y="0" width="482" height="320" fill="url(#skyline)"/>
      <rect x="300" y="30" width="170" height="260" rx="6" fill="url(#portrait)" opacity=".55"/>
    </g>
    <path d="M0,219 C160,270 360,230 482,139 L482,480 L0,480 Z" fill="var(--blue)"/>
    <path d="M0,275 C90,295 180,300 256,285 L256,340 L0,340 Z" fill="var(--grey-band)"/>
    <path d="M0,316 C90,325 190,325 256,300 L256,434 A30,30 0 0 0 286,464 L482,464 L482,677 L0,677 Z" fill="var(--white)"/>
  </svg>

  <span class="brand-mark" style="left:67px;top:26px;width:42px;height:42px;background:#c4c8cd"></span>
  <div class="brand-name" style="left:0;top:76px;width:176px;font-size:15px;color:var(--white)">Advisory Summit</div>

  <div class="abs headline">
    <div class="headline__bold">Boost your graduates’</div>
    <div class="headline__serif">EMPLOYABILITY AND<br>STARTING SALARIES</div>
    <div class="headline__with">with <b>AdvisorySummit.example</b></div>
  </div>

  <div class="abs career">
    <h2 class="section-title">Management consulting career:</h2>
    <ul class="ticks">
      <li>#1 career choice for graduates</li>
      <li>Biggest employer of top graduates</li>
      <li>Highest starting salaries outside banking</li>
    </ul>
    <p class="career__note">But only 1 in 30 applicants are successful without expert career advice.</p>
  </div>

  <div class="abs get">
    <h2 class="section-title">What you get:</h2>
    <ul class="get__list">
      <li class="get__item">
        <svg class="get__icon" viewBox="0 0 22 22"><circle cx="11" cy="11" r="10" fill="none" stroke="#fff" stroke-width="1.2"/><path d="M8 7.5 L15 11 L8 14.5 Z" fill="#fff"/></svg>
        50 ‘bite-sized’ videos on all aspects of recruitment
      </li>
      <li class="get__item">
        <svg class="get__icon" viewBox="0 0 22 22"><circle cx="11" cy="11" r="10" fill="none" stroke="#fff" stroke-width="1.2"/><rect x="7.5" y="6" width="7" height="10" rx="1" fill="none" stroke="#fff" stroke-width="1"/><path d="M9 9h4M9 11h4M9 13h3" stroke="#fff" stroke-width=".8"/></svg>
        15 downloadable templates, cheat-sheets and score-cards
      </li>
      <li class="get__item">
        <svg class="get__icon" viewBox="0 0 22 22"><circle cx="11" cy="11" r="10" fill="none" stroke="#fff" stroke-width="1.2"/><rect x="6.5" y="7" width="9" height="8" rx="1" fill="none" stroke="#fff" stroke-width="1"/><path d="M6.5 9.5h9M9 6v2M13 6v2" stroke="#fff" stroke-width=".9"/></svg>
        Live monthly Q&amp;A event for students
      </li>
      <li class="get__item">
        <svg class="get__icon" viewBox="0 0 22 22"><circle cx="11" cy="11" r="10" fill="none" stroke="#fff" stroke-width="1.2"/><circle cx="8.5" cy="9" r="1.8" fill="#fff"/><circle cx="13.5" cy="9" r="1.8" fill="#fff"/><path d="M5.5 15c0-2 1.4-3 3-3s3 1 3 3M10.5 15c0-2 1.4-3 3-3s3 1 3 3" fill="none" stroke="#fff" stroke-width="1"/></svg>
        Private online peer-support group
      </li>
    </ul>
  </div>

  <div class="abs advice">
    <h2 class="section-title">Expert insider advice on:</h2>
    <div class="advice__cols">
      <ul class="ticks advice__col">
        <li>Should you become a consultant?</li>
        <li>A day in the life of a consultant</li>
        <li>Consulting CVs</li>
        <li>Consulting interviews</li>
        <li>Consulting Covering Letters</li>
        <li>Partner Interviews</li>
        <li>Case Interviews</li>
        <li>Estimation interviews</li>
      </ul>
      <ul class="ticks advice__col">
        <li>Soft Skills &amp; Competences</li>
        <li>Psychometrics</li>
        <li>Group interviews</li>
        <li>Online assessments</li>
        <li>Best firms &amp; countries to work in</li>
        <li>How to progress</li>
        <li>The ‘up or out’ policy</li>
        <li>Networking for success</li>
      </ul>
    </div>
  </div>

  <footer class="footer">
    <div class="footer__item">
      <svg width="10" height="7" viewBox="0 0 10 7"><rect width="10" height="7" rx="1" fill="var(--blue)"/><path d="M0.5 0.8 L5 4 L9.5 0.8" fill="none" stroke="#fff" stroke-width=".8"/></svg>
      max@advisorysummit.example
    </div>
    <span class="footer__divider"></span>
    <div class="footer__item">
      <svg width="10" height="10" viewBox="0 0 10 10"><circle cx="5" cy="5" r="4.3" fill="none" stroke="var(--blue)" stroke-width="1"/><path d="M0.7 5h8.6M5 0.7c-2 2.5-2 6 0 8.6M5 0.7c2 2.5 2 6 0 8.6" fill="none" stroke="var(--blue)" stroke-width=".8"/></svg>
      www.advisorysummit.example
    </div>
  </footer>
</section>

<!-- BACK -->
<section class="page page--back">
  <svg class="page-bg" viewBox="0 0 482 677">
    <defs>
      <linearGradient id="meeting" x1="0" y1="0" x2="1" y2="0">
        <stop offset="0" stop-color="#d9dde0"/>
        <stop offset=".5" stop-color="#eef0f1"/>
        <stop offset="1" stop-color="#c9ccd0"/>
      </linearGradient>
    </defs>
    <rect role="img" aria-label="Photo of a stressed graduate facing a senior interviewer across a table" x="0" y="0" width="482" height="230" fill="url(#meeting)"/>
    <path d="M0,130 C150,170 360,140 482,56 L482,240 L0,240 Z" fill="var(--blue)"/>
    <path d="M0,180 C150,225 330,205 482,110 L482,240 L0,240 Z" fill="var(--grey-band)"/>
    <path d="M0,190 C150,238 330,222 482,122 L482,677 L0,677 Z" fill="var(--white)"/>
  </svg>

  <span class="brand-mark" style="left:396px;top:164px;width:36px;height:36px;background:var(--grey)"></span>
  <div class="brand-name" style="left:344px;top:205px;width:140px;font-size:12px;color:var(--grey)">Advisory Summit</div>

  <div class="abs bio">
    <h1 class="bio__name">PROF. MAX WHITFIELD</h1>
    <p class="bio__text">Is an ex-consultant &amp; recruiter who has worked with or for all the major consultancies. He is now a Professor of Consulting and has helped over 700 students land consulting jobs. Max wrote the world’s best-selling textbook on consultancy and his courses on consultancy have won national and international awards.</p>
  </div>

  <div class="abs pricing">
    <h2 class="section-title">Pricing</h2>
    <ul class="ticks pricing__grid">
      <li>100 licences: £2500</li>
      <li>500 licences: £3500</li>
      <li>1000 licences: £4000</li>
      <li>Unlimited licences: £4500</li>
    </ul>
  </div>

  <div class="workshops-band"></div>
  <div class="abs workshops">
    <h2 class="section-title">Workshops &amp; Talks</h2>
    <p class="workshops__text">Prof. Max Whitfield also provides independent, expert workshops and talks on any aspect of management consulting. These have been delivered at several top Universities including Ashford, Wexley, Carrow &amp; Linden Universities:</p>
    <div class="workshops__cols">
      <ul class="ticks">
        <li>What are the pros and cons of management consulting?</li>
        <li>How to land the dream consulting career</li>
        <li>How to master the case-interview, the partner interview and behavioural tests</li>
      </ul>
      <ul class="ticks">
        <li>The truth about the Big 4 &amp; MBB</li>
        <li>A deep dive on international consulting work</li>
        <li>Stories and warnings from the consulting coal-face</li>
      </ul>
    </div>
  </div>

  <div class="abs feedback">
    <h2 class="feedback__title">FEEDBACK &amp; TESTIMONIALS</h2>
    <div class="feedback__cols">
      <div class="feedback__col">
        <p class="quote">‘Honestly, without Max’s course I wouldn’t have landed a consulting job at all, let alone this one’ – <cite>Elena, Northbridge Advisory.</cite></p>
        <p class="quote">‘Max’s insights into the recruitment process, especially the case and partner interviews, were crucial in my offer at Kestrel Partners’ – <cite>Sam, Kestrel Partners.</cite></p>
        <p class="quote">‘Your delivery of honest, relevant and timely advice to students considering a career in management consulting is really appreciated by students and staff alike, and we hope to continue this successful relationship in future years’. <cite>Course Director, Redfield Business School.</cite></p>
      </div>
      <div class="feedback__col">
        <p class="quote">‘Max is the best teacher I’ve had. What he doesn’t know about the consulting industry isn’t worth knowing’ – <cite>Antoine, Harlow Strategy.</cite></p>
        <p class="quote">‘The insider tips, CV scorer and behavioural interview templates were SO useful. Thank you so much. Your advice about the interviews was spot-on, even down to some of the questions they asked!’ <cite>Nisa, Corvane &amp; Co.</cite></p>
        <p class="quote">‘The feedback after the interview was great, and they especially liked the questions you suggested around utilisation and leverage. Thank you!’ <cite>Simon, Ledger &amp; Pike.</cite></p>
      </div>
    </div>
  </div>

  <footer class="footer">
    <div class="footer__item">
      <svg width="10" height="7" viewBox="0 0 10 7"><rect width="10" height="7" rx="1" fill="var(--blue)"/><path d="M0.5 0.8 L5 4 L9.5 0.8" fill="none" stroke="#fff" stroke-width=".8"/></svg>
      max@advisorysummit.example
    </div>
    <span class="footer__divider"></span>
    <div class="footer__item">
      <svg width="10" height="10" viewBox="0 0 10 10"><circle cx="5" cy="5" r="4.3" fill="none" stroke="var(--blue)" stroke-width="1"/><path d="M0.7 5h8.6M5 0.7c-2 2.5-2 6 0 8.6M5 0.7c2 2.5 2 6 0 8.6" fill="none" stroke="var(--blue)" stroke-width=".8"/></svg>
      www.advisorysummit.example
    </div>
  </footer>
</section>

</body>
</html>
```